New Website Design (Uncoded) Competition for Velto Trade Link

Please submit design concepts for a Joomla 3.0 Website for VELTO TRADE LINK company. Our client prefers a modem style design, responsive to all mobile devices,
The website demo content needs to be clear and detailed.

Menu sample:
Home/About Us/Service/Strength/Partner/News/Contact US/Blog

Requirements:
1. Only need to submit the PSD for the design, coding work is not included.
2. Please submit both Homepage and Inner page to demonstrate the concept.
3. The Homepage needs to include: LOGO/MENU/Banner/Language Switcher/Company Introduction/Welcome module/Advertising Module/Footer Menu/Footer/Copyright/Social Links
4. Use Asian business women for demo pictures/Could try city pictures for background.
5. Prefer SINGLE SCREEN design rather than scrollable multiple screen designs.
6. Avoid any chain symbol since the company is more about financial business.
7. Avoid any direct connotations related with money or cash.
Updates

Hi Designers, I have clearly state the requirements that avoid using neg connontation pictures like cash/ property, though still receive concepts like that. Please check the brief clearly and mark at Update with "cheers" Kip from LW

Target Market(s)

Shenzhen Dorvik Velto Trade link Company provide cross-border Supply chain Financial service by integrating Dorvik Trade Link resource.
The Company mission is become the most respectful, professional and valuable Chinese Supply Chain Financial Company, pioneer the supply chain industry.

Industry/Entity Type

Financial

Font styles to use
Sans Serif

Colors
33b7a4

Requirements
Must have
• 1. Necessary Web element, including Logo/navigation/ Banner/ Footer
2. Asia business Women pictures.
Should not have
• 6. Avoid any chain symbol since the company is more about financial business.

```html
<!DOCTYPE html>
<html lang="en">
<head>
<meta charset="utf-8">
<title>Velto Trade Link</title>
<link href="https://fonts.googleapis.com/css2?family=Jost:wght@400;500&family=Open+Sans:wght@400;600&display=swap" rel="stylesheet">
<style>
:root{
  --blue:#2a8fd3;
  --blue-dark:#1f7cc0;
  --nav:#2b2b2b;
  --gray-text:#555;
  --light:#f3f3f3;
  --footer:#3c3c3c;
  --white:#fff;
}
*{margin:0;padding:0;box-sizing:border-box}
html,body{width:929px;height:1200px;overflow:hidden;background:var(--white)}
body{position:relative;font-family:Arial,Helvetica,sans-serif;color:#333}
.abs{position:absolute}
.brand{display:flex;align-items:center;gap:10px;font-family:'Jost',sans-serif;font-weight:500;letter-spacing:1px;white-space:nowrap}
.brand-mark{width:26px;height:26px;background:var(--blue);flex:none}
.site-brand{left:80px;top:22px;font-size:26px;color:var(--gray-text)}
.lang{left:718px;top:18px;width:134px;height:25px;background:var(--blue);border-radius:3px;color:#fff;font-size:10px;line-height:25px;padding-left:6px}
.lang .caret{position:absolute;right:5px;top:4px;width:17px;height:17px;background:#fff;border-radius:2px}
.lang .caret:after{content:"";position:absolute;left:4px;top:6px;border:4.5px solid transparent;border-top:5px solid var(--blue)}
.phone{right:77px;top:60px;display:flex;align-items:center;gap:6px;font-family:'Open Sans',sans-serif;font-size:19px;color:var(--gray-text)}
.phone b{color:var(--blue);font-weight:600}
.nav{left:0;top:98px;width:929px;height:34px;background:var(--nav)}
.nav a{position:absolute;top:0;line-height:34px;color:#fff;font-family:'Open Sans',sans-serif;font-size:11.5px;text-decoration:none}
.nav a.active{background:var(--blue);top:5px;height:25px;line-height:25px;padding:0 8px}
.dropdown{left:200px;top:141px;width:160px;height:81px;background:#2f3236;padding:17px 9px 0 7px;z-index:3}
.dropdown:before{content:"";position:absolute;left:74px;top:-7px;border:7px solid transparent;border-top:0;border-bottom-color:#2f3236}
.dropdown div{height:23px;margin-bottom:6px;border-radius:2px;background:#1e2023;color:#fff;font-size:9px;line-height:23px;padding-left:15px;font-family:'Open Sans',sans-serif;position:relative}
.dropdown div:before{content:"";position:absolute;left:8px;top:8px;border:3px solid transparent;border-left:4px solid #fff;border-right:0}
.dropdown div.on{background:var(--blue)}
.hero-band{left:0;top:132px;width:929px;height:618px;background:var(--blue)}
.banner{left:78px;top:162px;width:773px;height:343px;background:#fff;padding:6px}
.banner-photo{width:100%;height:100%;background:linear-gradient(100deg,#c8cdd1 0%,#e6e8ea 45%,#9ea3a8 60%,#f2f2f2 100%)}
.banner-shadow{left:95px;top:500px;width:740px;height:40px;border-radius:50%;background:radial-gradient(ellipse at center,rgba(0,40,80,.45),rgba(0,40,80,0) 70%)}
.caption{left:99px;top:240px;width:376px;height:176px;background:rgba(70,75,80,.6);padding:12px 24px;color:#fff}
.caption h1{font-family:'Jost',sans-serif;font-weight:400;font-size:32px;line-height:38px}
.caption p{font-size:12px;line-height:18.5px;margin-top:6px}
.btn{display:inline-block;margin-top:12px;width:104px;height:32px;border:2px solid #fff;border-radius:4px;background:var(--blue);font-family:'Jost',sans-serif;font-size:17px;line-height:28px;text-align:center}
.team-photo{left:74px;top:574px;width:238px;height:148px;background:#fff;padding:4px;border:1px solid #ddd}
.team-photo div{width:100%;height:100%;background:linear-gradient(180deg,#f4f4f4,#cfd3d6 60%,#4a4f56)}
.welcome{left:334px;top:568px;width:517px;color:#fff}
.welcome h2{font-family:'Jost',sans-serif;font-weight:400;font-size:22px;letter-spacing:.3px}
.welcome p{font-size:10.4px;line-height:15.6px;text-align:justify;margin-top:4px}
.welcome p+p{margin-top:15px}
.heading{font-family:'Jost',sans-serif;font-weight:500;font-size:21px;color:var(--gray-text)}
.heading span{color:var(--blue)}
.card{top:830px;width:200px;height:258px;background:#fff;box-shadow:0 0 3px rgba(0,0,0,.15)}
.card-photo{height:130px}
.card h3{font-family:'Open Sans',sans-serif;font-weight:400;font-size:13px;margin:8px 8px 0;padding-bottom:4px;border-bottom:1px solid #999;color:#222}
.card p{font-size:10px;line-height:17px;margin:10px 8px 0;color:#222}
.card-meta{position:absolute;left:0;bottom:0;width:100%;height:34px;background:var(--light);display:flex;align-items:center;padding-left:10px;font-family:'Open Sans',sans-serif;font-size:10px;color:#777;gap:6px}
.card-meta .date{color:var(--blue)}
.card-meta .sep{width:1px;height:15px;background:#999;margin:0 6px}
.ad{left:552px;top:829px;width:299px;height:249px;border:1px solid #ccc;padding:2px}
.ad div{width:100%;height:100%;background:linear-gradient(160deg,#0d3f8a,#1d6ac0 55%,#d7e6f2)}
.footer{left:0;top:1118px;width:929px;height:82px;background:var(--footer)}
.foot-links{left:82px;top:1136px;font-family:'Open Sans',sans-serif;font-size:9.6px;color:#fff;word-spacing:2px}
.foot-links i{font-style:normal;margin:0 7px;color:#ccc}
.copy{left:82px;top:1167px;font-size:11px;color:#fff}
.divider{left:357px;top:1156px;height:36px;border-left:1px dotted #777}
.social{top:1162px;width:22px;height:22px;border-radius:50%}
.foot-brand{right:78px;top:1144px;font-size:21px;gap:8px;color:#e8e8e8}
.foot-brand .brand-mark{width:22px;height:22px;background:#cfcfcf}
</style>
</head>
<body>
<header>
  <div class="abs brand site-brand"><span class="brand-mark"></span>VELTO TRADE LINK</div>
  <div class="abs lang">Select your Language<span class="caret"></span></div>
  <div class="abs phone">
    <svg width="16" height="16" viewBox="0 0 24 24"><path fill="#333" d="M6.6 10.8a15 15 0 0 0 6.6 6.6l2.2-2.2c.3-.3.7-.4 1-.2 1.1.4 2.3.6 3.6.6.6 0 1 .4 1 1V20c0 .6-.4 1-1 1A17 17 0 0 1 3 4c0-.6.4-1 1-1h3.5c.6 0 1 .4 1 1 0 1.3.2 2.5.6 3.6.1.3 0 .7-.2 1z"/></svg>
    <span><b>CALL :</b> 555-204(7319)</span>
  </div>
</header>
<nav class="abs nav">
  <a style="left:91px">HOME</a>
  <a style="left:165px">ABOUT US</a>
  <a class="active" style="left:250px">SERVICE</a>
  <a style="left:341px">STRENGTH</a>
  <a style="left:437px">PARTNER</a>
  <a style="left:524px">NEWS</a>
  <a style="left:595px">CONTACT US</a>
  <a style="left:702px">BLOG</a>
</nav>
<div class="abs dropdown"><div class="on">Lorem Ipsum</div><div>Lorem Ipsum sed</div></div>

<section class="abs hero-band"></section>
<div class="abs banner-shadow"></div>
<div class="abs banner"><div class="banner-photo" role="img" aria-label="Smiling Asian businesswoman on a phone holding a folder, office buildings behind"></div></div>
<div class="abs caption">
  <h1>LOREM IPSUM DOLOR</h1>
  <p>Duis aute irure dolor in reprehenderit in voluptate velit esse cillum dolore eu fugiat nulla pariatur.&nbsp; sunt in culpa qui officia deserunt mollit anim id est laborum.</p>
  <span class="btn">Read More</span>
</div>

<div class="abs team-photo"><div role="img" aria-label="Group of Asian business people posing around a desk with a laptop"></div></div>
<div class="abs welcome">
  <h2>WELCOME TO VELTO TRADE LINK</h2>
  <p>Sed ut perspiciatis unde omnis iste natus error sit voluptatem accusantium doloremque laudantium, totam rem aperiam, eaque ipsa quae ab illo inventore veritatis et quasi architecto beatae vitae dicta sunt explicabo. Nemo enim ipsam voluptatem quia voluptas sit aspernatur aut odit aut fugit, sed quia consequuntur magni dolores eos qui ratione voluptatem sequi nesciunt.</p>
  <p>Neque porro quisquam est, qui dolorem ipsum quia dolor sit amet, consectetur, adipisci velit, sed quia non numquam eius modi tempora incidunt ut labore et dolore magnam aliquam quaerat voluptatem. Ut enim ad consequatur, vel illum qui dolorem eum fugiat quo voluptas nulla pariatur</p>
</div>

<h2 class="abs heading" style="left:78px;top:784px"><span>OUR</span> BLOG</h2>
<h2 class="abs heading" style="left:552px;top:783px"><span>ADVERTISING</span> MODULE</h2>

<article class="abs card" style="left:78px">
  <div class="card-photo" role="img" aria-label="Business people shaking hands over a table with charts" style="background:linear-gradient(135deg,#6f6a64,#d9d9d6 50%,#3b3b3b)"></div>
  <h3>LOREM IPSUM</h3>
  <p>natus aperiam, eaque ipsa quae ab illo inventore dicta sunt explicabo.</p>
  <div class="card-meta"><span>&#9633;</span><span class="date">May 11, 2014</span><span class="sep"></span><span>&#9711;</span><span>Comment</span></div>
</article>
<article class="abs card" style="left:311px">
  <div class="card-photo" role="img" aria-label="Asian businesswoman at a computer in an office with colleagues" style="background:linear-gradient(135deg,#eeeeee,#c8c8c8 50%,#1b2d5c)"></div>
  <h3>LOREM IPSUM</h3>
  <p>natus aperiam, eaque ipsa quae ab illo inventore dicta sunt explicabo.</p>
  <div class="card-meta"><span>&#9633;</span><span class="date">May 11, 2014</span><span class="sep"></span><span>&#9711;</span><span>Comment</span></div>
</article>

<aside class="abs ad"><div role="img" aria-label="Advertising banner about screening job candidates with video interviews"></div></aside>

<footer class="abs footer"></footer>
<div class="abs foot-links">Home<i>/</i>About Us<i>/</i>Service<i>/</i>Strength<i>/</i>Partner<i>/</i>News<i>/</i>Contact US<i>/</i>Blog</div>
<div class="abs copy">Copyright © 2014 All Rights Reserved | Privacy Policy</div>
<div class="abs divider"></div>
<span class="abs social" style="left:377px;background:#1d4f8f" aria-label="Social link"></span>
<span class="abs social" style="left:408px;background:#1d9ce0" aria-label="Social link"></span>
<span class="abs social" style="left:439px;background:#ee8a1b" aria-label="Feed link"></span>
<span class="abs social" style="left:470px;background:#9a9a9a" aria-label="Email link"></span>
<div class="abs brand foot-brand"><span class="brand-mark"></span>VELTO TRADE LINK</div>
</body>
</html>
```